Design a Website Mockup for Kids Social Media site

UPDATE: I have chosen a winning logo from another contest, and have now attached the logo to this contest for use in the mockups.

The name of website I require a mockup created for is 'Pun Parade', but it is actually to be written as a single word as the url is punparade.com.

*This is for kids 5-12 years old. Needs to be easy to navigate for beginner computer and tablet users.

*Site will be responsive, better chance of winning contest with mockup on screen, tablet and mobile.

*Sample theme/style can be seen at the website http://www.tvq.net.au/tvqforlittles/.or any website for young kids

*Bright primary and secondary paint colours are to be used (Yellow, Red, Blue, Orange, Green, Purple).

*The background will have themes, the user can choose from a rainbow, or a blue sky and fluffy white clouds, etc. Pick one or both of rainbow and/or blue sky + clouds.

*Sample jokes for content filling at http://www.gigglebarn.com/jokes/one_liner_jokes/funny_questions_and_answers (also happy with Lorem Ipsum...)

Description of the site - A social network style site which allows users to share jokes with each other, the sharing (called swapping) of the jokes is the primary function of the site.

I have attached 4 slightly different wireframes, you can choose a single preference, all four layouts or offer an alternate with the same components.

```html
<!DOCTYPE html>
<html lang="en">
<head>
<meta charset="utf-8">
<title>PunParade – Swap Jokes</title>
<link rel="stylesheet" href="https://fonts.googleapis.com/css2?family=Fredoka+One&family=Open+Sans:wght@400;600;700&display=swap">
<style>
:root{
  --sky:#c4e2ec;
  --sky-deep:#a9d3e2;
  --blue:#1a87cd;
  --blue-dark:#1270ad;
  --green:#7ab648;
  --green-dark:#2f9f57;
  --orange:#f4a118;
  --orange-deep:#ef7a2c;
  --purple:#8a1670;
  --yellow:#fbd40f;
  --red:#e4222a;
  --ink:#555;
  --white:#fff;
}
*{box-sizing:border-box;margin:0;padding:0}
html,body{width:870px;height:1200px;overflow:hidden}
body{font-family:'Open Sans',Arial,sans-serif;color:var(--ink)}
.canvas{position:relative;width:870px;height:1200px;overflow:hidden;
  background:
   radial-gradient(ellipse 90px 40px at 120px 560px,rgba(255,255,255,.45),transparent 70%),
   radial-gradient(ellipse 110px 45px at 40px 700px,rgba(255,255,255,.4),transparent 70%),
   radial-gradient(ellipse 120px 50px at 840px 480px,rgba(255,255,255,.45),transparent 70%),
   radial-gradient(ellipse 100px 40px at 850px 230px,rgba(255,255,255,.4),transparent 70%),
   radial-gradient(ellipse 130px 50px at 430px 480px,rgba(255,255,255,.35),transparent 70%),
   linear-gradient(180deg,var(--sky) 0%,#cfe8f0 40%,var(--sky-deep) 100%);}
.top-stripe{position:absolute;left:0;top:0;width:870px;height:3px;
  background:linear-gradient(90deg,var(--orange) 0 12%,var(--green) 12% 24%,var(--blue) 24% 36%,var(--purple) 36% 48%,var(--yellow) 48% 60%,var(--red) 60% 72%,var(--blue) 72% 84%,var(--green) 84% 100%)}
.abs{position:absolute}
.login{left:64px;top:18px;font-size:11px;color:var(--purple)}
.contact-line{right:152px;font-size:10px;display:flex;align-items:center;gap:10px}
.contact-line.email{top:18px;color:var(--orange)}
.contact-line.phone{top:38px;color:var(--blue)}
.profile{left:707px;top:16px;display:flex;align-items:center;gap:9px;font-size:11px;color:var(--red)}
.profile .avatar{width:36px;height:36px;border-radius:50%;background:var(--red);display:flex;align-items:center;justify-content:center}
.logo{left:64px;top:60px;font-family:'Fredoka One',cursive;font-size:33px;color:var(--red);line-height:36px}
.nav{left:403px;top:63px;display:flex;gap:3px}
.nav a{display:block;height:35px;line-height:35px;text-align:center;color:#fff;font-size:11px;text-decoration:none;text-transform:uppercase}
.nav .about{width:80px;background:var(--orange)}
.nav .activities{width:83px;background:var(--blue)}
.nav .rooms{width:71px;background:var(--purple)}
.nav .pages{width:67px;background:var(--yellow)}
.nav .contacts{width:87px;background:var(--green)}
.panel{position:absolute;border-radius:3px}
.swap-form{left:65px;top:142px;width:246px;height:326px;background:var(--blue);padding:18px 16px 0 22px}
.swap-form h2{font-family:'Fredoka One',cursive;color:#fff;font-size:24px;font-weight:400;letter-spacing:.5px}
.swap-form p{color:#fff;font-size:11px;line-height:15px;margin:6px 0 10px}
.field{background:#fff;border-radius:3px;height:35px;margin-bottom:7px;font-size:10px;color:var(--blue);padding:9px 12px;position:relative}
.field.tall{height:61px}
.field .caret{position:absolute;right:12px;top:14px}
.hero{left:326px;top:142px;width:481px;height:326px;overflow:hidden;
  background:linear-gradient(180deg,#2f7fd0 0%,#6fb0e6 35%,#e7c55a 55%,#7cc63c 72%,#3c9a2a 100%)}
.hero .art{position:absolute;inset:0}
.dots{position:absolute;left:220px;bottom:10px;display:flex;gap:4px}
.dots span{width:10px;height:10px;border-radius:50%;background:var(--red)}
.dots span:last-child{background:var(--purple)}
.story{left:65px;top:499px;width:246px;height:385px;background:var(--green);padding:0 20px}
.photo-frame{position:absolute;left:22px;top:30px;width:202px;height:170px;background:#fff;box-shadow:2px 3px 6px rgba(0,0,0,.2);padding:8px}
.photo-frame::before{content:"";position:absolute;inset:-5px 4px 6px -6px;background:#fff;transform:rotate(-2deg);z-index:-1;box-shadow:1px 2px 4px rgba(0,0,0,.15)}
.photo-frame .img{width:100%;height:100%;background:linear-gradient(135deg,#dff4f8,#c8e6ee 60%,#e8c39a)}
.story h3{position:absolute;left:20px;top:220px;font-family:'Fredoka One',cursive;font-weight:400;color:#fff;font-size:15px}
.story p{position:absolute;left:20px;top:246px;width:206px;color:#fff;font-size:9px;line-height:12px}
.read-more{font-family:'Fredoka One',cursive;font-size:10px}
.story .read-more{position:absolute;left:20px;top:342px;color:#fff}
.activity{left:313px;top:499px;width:244px;height:385px;background:var(--orange)}
.joke-card{position:absolute;left:23px;top:30px;width:200px;height:301px;background:#fff;box-shadow:0 3px 6px rgba(0,0,0,.15)}
.joke-card h3{font-family:'Fredoka One',cursive;font-weight:400;font-size:13px;color:var(--green);text-align:center;margin:22px 0 16px}
.joke-list{list-style:none}
.joke-list li{display:flex;align-items:center;gap:10px;height:40px;border-left:3px solid;border-bottom:1px dotted #ddd;padding-left:12px;font-size:8.5px;line-height:12px}
.num{flex:none;width:24px;height:24px;border-radius:50%;color:#fff;font-family:'Fredoka One',cursive;font-size:13px;display:flex;align-items:center;justify-content:center;box-shadow:0 0 0 3px #e9eef0}
.c-blue{color:var(--blue);border-color:var(--blue)}.c-blue .num{background:#3ba6de}
.c-green{color:var(--green-dark);border-color:var(--green-dark)}.c-green .num{background:var(--green-dark)}
.c-orange{color:var(--orange);border-color:var(--orange-deep)}.c-orange .num{background:var(--orange-deep)}
.c-purple{color:var(--purple);border-color:var(--purple)}.c-purple .num{background:#c33fb0}
.joke-card .read-more{position:absolute;left:18px;bottom:18px;color:var(--orange)}
.friends{left:559px;top:499px;width:246px;height:385px;background:var(--blue);text-align:center;color:#fff}
.friend-ring{position:absolute;left:32px;top:26px;width:180px;height:180px;border-radius:50%;background:#fff;box-shadow:14px 0 0 #e6f0b8,-6px 0 0 #bfe6f3}
.friend-ring .img{position:absolute;inset:10px;border-radius:50%;border:1px dashed #ccc;background:linear-gradient(180deg,#cfe3ee 0%,#b9c9cf 55%,#d6c2ad 100%)}
.friends h3{position:absolute;top:220px;width:100%;font-family:'Fredoka One',cursive;font-weight:400;font-size:19px}
.friends .lead{position:absolute;top:251px;width:100%;font-size:10.5px}
.friends hr{position:absolute;left:62px;top:275px;width:120px;border:0;border-top:1px solid #fff}
.friends .body{position:absolute;left:22px;top:285px;width:202px;font-size:9px;line-height:13px}
.pager{position:absolute;left:91px;top:334px;display:flex}
.pager span{width:24px;height:24px;display:flex;align-items:center;justify-content:center}
.bg-purple{background:var(--purple)}.bg-yellow{background:var(--yellow)}
.captcha{left:65px;top:907px;width:246px;height:208px;background:var(--purple);color:#fff;text-align:center}
.captcha h3{position:absolute;left:27px;top:20px;font-family:'Fredoka One',cursive;font-weight:400;font-size:14px}
.captcha .face{position:absolute;left:79px;top:51px;width:80px;height:80px;border-radius:50%;border:3px solid #fff;background:linear-gradient(160deg,#9fcf6a,#c7a08c 50%,#d23b37)}
.captcha .arrow{position:absolute;top:93px;width:24px;height:24px;display:flex;align-items:center;justify-content:center}
.captcha p{position:absolute;left:30px;top:142px;width:186px;font-size:9px;line-height:13px}
.captcha .tools{position:absolute;left:0;top:178px;width:100%;display:flex;justify-content:center;gap:18px}
.answers{left:313px;top:907px;width:493px;height:208px;background:var(--red)}
.answer-card{position:absolute;left:17px;top:17px;width:459px;height:174px;background:#fff;padding:18px 19px 0}
.answer-card h3{font-family:'Fredoka One',cursive;font-weight:400;font-size:13px;color:var(--orange);margin-bottom:12px}
.answer-list{list-style:none}
.answer-list li{display:flex;align-items:center;gap:14px;height:36px;border-left:2px solid;border-bottom:1px dotted #ddd;padding-left:16px;font-size:8.5px;line-height:12px}
.answer-list .text{width:280px}
.show-all{margin-left:auto;width:70px;height:24px;color:#fff;font-family:'Fredoka One',cursive;font-size:8.5px;display:flex;align-items:center;justify-content:center}
.c-blue .show-all{background:var(--blue)}.c-green .show-all{background:var(--green-dark)}.c-orange .show-all{background:var(--orange-deep)}
.footer{position:absolute;left:0;top:1158px;width:870px;height:42px;background:var(--green);color:#fff;font-size:10px;display:flex;align-items:center;padding:0 64px}
</style>
</head>
<body>
<div class="canvas">
  <div class="top-stripe"></div>

  <header>
    <div class="abs login">Login to create Account</div>
    <div class="abs contact-line email">hello@kidschatter.com
      <svg width="11" height="9" viewBox="0 0 11 9"><rect x=".5" y=".5" width="10" height="8" fill="none" stroke="#f4a118"/><path d="M.5 .5l5 4 5-4" fill="none" stroke="#f4a118"/></svg>
    </div>
    <div class="abs contact-line phone">+1 555 014 2290
      <svg width="10" height="10" viewBox="0 0 10 10"><path d="M2 .5l2 2.2-1 1.3a6 6 0 0 0 3 3l1.3-1 2.2 2-1.3 1.5C4.5 9.5.5 5.5.5 1.8z" fill="#1a87cd"/></svg>
    </div>
    <div class="abs profile">
      <span class="avatar"><svg width="14" height="15" viewBox="0 0 14 15"><circle cx="7" cy="4" r="3.5" fill="#fff"/><path d="M0 15c0-4 3-6 7-6s7 2 7 6z" fill="#fff"/></svg></span>
      Profile
      <svg width="10" height="6" viewBox="0 0 10 6"><path d="M1 1l4 4 4-4" fill="none" stroke="#e4222a" stroke-width="1.6"/></svg>
    </div>
    <div class="abs logo">PunParade</div>
    <nav class="abs nav">
      <a class="about" href="#">About Us</a>
      <a class="activities" href="#">Activities</a>
      <a class="rooms" href="#">Rooms</a>
      <a class="pages" href="#">Pages</a>
      <a class="contacts" href="#">Contacts</a>
    </nav>
  </header>

  <section class="panel swap-form">
    <h2>FUNNY</h2>
    <p>Lorem ipsum dolor sit amet conse ctetur adip-isicing elit, sed do eiusmod tempo !</p>
    <div class="field">Your Name</div>
    <div class="field">Your Secret Word
      <svg class="caret" width="11" height="7" viewBox="0 0 11 7"><path d="M0 0h11L5.5 7z" fill="#1a87cd"/></svg>
    </div>
    <div class="field tall">Joke Question</div>
    <div class="field tall">Answer</div>
  </section>

  <section class="panel hero">
    <div class="art" role="img" aria-label="Illustration of three cartoon kids with phones and a laptop in a green meadow under a rainbow"></div>
    <div class="dots"><span></span><span></span><span></span></div>
  </section>

  <section class="panel story">
    <div class="photo-frame"><div class="img" role="img" aria-label="Photo of three young men juggling oranges"></div></div>
    <h3>LOREM IPSUM</h3>
    <p>Lorem Ipsum is simply dummy text of the printing and typesetting industry. Lorem Ipsum has been the industry's standard dummy text ever since the 1500s, when an unknown printer took a galley of type and scrambled it to make a type specimen book. It has survived not only five centuries, but also the leap !</p>
    <span class="read-more">Read More</span>
  </section>

  <section class="panel activity">
    <div class="joke-card">
      <h3>ACTIVITY JOKES</h3>
      <ol class="joke-list">
        <li class="c-blue"><span class="num">1</span>How can you drop a raw egg onto a concrete floor ?</li>
        <li class="c-green"><span class="num">2</span>How can you lift an elephant with one hand?</li>
        <li class="c-orange"><span class="num">3</span>How can a man go eight days without sleep?</li>
        <li class="c-blue"><span class="num">4</span>How can a man go eight days without sleep?</li>
        <li class="c-purple"><span class="num">5</span>Why it is impossible to send a telegram to Washington today?</li>
      </ol>
      <span class="read-more">Read More</span>
    </div>
  </section>

  <section class="panel friends">
    <div class="friend-ring"><div class="img" role="img" aria-label="Photo of two small children hugging on a beach, seen from behind"></div></div>
    <h3>Friend List</h3>
    <div class="lead">It is a long established fact that a reader</div>
    <hr>
    <p class="body">Lorem Ipsum is simply dummy text of the printing and typesetting industry. Lorem Ipsum has been the industry's standard dummy =</p>
    <div class="pager">
      <span class="bg-purple"><svg width="6" height="10" viewBox="0 0 6 10"><path d="M5 1L1 5l4 4" fill="none" stroke="#fff" stroke-width="1.5"/></svg></span>
      <span class="bg-yellow"><svg width="6" height="10" viewBox="0 0 6 10"><path d="M1 1l4 4-4 4" fill="none" stroke="#fff" stroke-width="1.5"/></svg></span>
    </div>
  </section>

  <section class="panel captcha">
    <h3>Fun Captcha</h3>
    <div class="face" role="img" aria-label="Photo of a laughing young boy"></div>
    <span class="arrow" style="left:0;background:var(--blue)"><svg width="6" height="10" viewBox="0 0 6 10"><path d="M5 1L1 5l4 4" fill="none" stroke="#fff" stroke-width="1.5"/></svg></span>
    <span class="arrow" style="right:0;background:var(--orange)"><svg width="6" height="10" viewBox="0 0 6 10"><path d="M1 1l4 4-4 4" fill="none" stroke="#fff" stroke-width="1.5"/></svg></span>
    <p>Lorem Ipsum is simply dummy text of the printing and typesetting industry.</p>
    <div class="tools">
      <svg width="10" height="12" viewBox="0 0 10 12"><path d="M2 3.5a3 3 0 1 1 4 2.8c-1 .4-1 1-1 2" fill="none" stroke="#fff" stroke-width="1.6"/><circle cx="5" cy="11" r="1" fill="#fff"/></svg>
      <svg width="12" height="12" viewBox="0 0 12 12"><path d="M10 4a4.5 4.5 0 0 0-8 0M2 8a4.5 4.5 0 0 0 8 0" fill="none" stroke="#fff" stroke-width="1.5"/><path d="M10 1v3H7M2 11V8h3" fill="none" stroke="#fff" stroke-width="1.5"/></svg>
      <svg width="12" height="12" viewBox="0 0 12 12"><path d="M1.5 8V6a4.5 4.5 0 0 1 9 0v2" fill="none" stroke="#fff" stroke-width="1.5"/><rect x="1" y="7" width="3" height="4" fill="#fff"/><rect x="8" y="7" width="3" height="4" fill="#fff"/></svg>
    </div>
  </section>

  <section class="panel answers">
    <div class="answer-card">
      <h3>JOKE ANSWER</h3>
      <ol class="answer-list">
        <li class="c-blue"><span class="num">1</span><span class="text">Lorem Ipsum is simply dummy text of the printing and typesetting industry. Lorem Ipsum has been the industry's standard .</span><span class="show-all">SHOW ALL</span></li>
        <li class="c-green"><span class="num">2</span><span class="text">Lorem Ipsum is simply dummy text of the printing and typesetting industry. Lorem Ipsum has been the industry's standard .</span><span class="show-all">SHOW ALL</span></li>
        <li class="c-orange"><span class="num">3</span><span class="text">Lorem Ipsum is simply dummy text of the printing and typesetting industry. Lorem Ipsum has been the industry's standard .</span><span class="show-all">SHOW ALL</span></li>
      </ol>
    </div>
  </section>

  <footer class="footer">Copyright@2015 | All Reserved</footer>
</div>
</body>
</html>
```